GULL REEF DISTILLERY BOTTLE LABELS

Hello Designers,

I would like to see the bottles literally be labeled as an absolute stand out from any competitor, incorporating eye-catching copper colour label background colour which matches the colour of my two Copper Pot Stills.

Front Label will be black font on copper label
saying:-

Gull Reef Distillery

A "mm♡" water mark to be incorporated on main label (example attached)

Plus an outline of Gull Reef, (located in Tasmania, Australia), suttle and cleverly included, but only to those who are particularly observant.

I also have visualised Angel wings in a copper outline with diamond details (photo of my necklace attached), incorporated with the two 55L copper stills (photo attached).

I have taken a photo of the Velvet Heron Stills (as attached file ‘outline') and have done my best to edit it to show that I would just like the outline to be shown for the copper coloured label (no hoses or shadows should be in it).

Naturally, there are other labels needed to compliment the main Label on the bottle of spirit. For reference much of the rest of the standard information will be very similar to labels on other bottles in any bottle shop.

The Gull Reef Distillery label separate to the Main Brand logo will be a different colour background & font

a Front) Gin Spirit Label)) - Blue colour font
Title = Gull Reef Native Gin
_______ ml - Crafted to enjoy now
%Alc Vol _______ Standard Drinks ________

b Front Label) Vodka Spirit Label )) - Ruby colour font
Title = Gull Reef Ruby Vodka
Crafted to enjoy now
____ ml ____%Alc Vol ____ Standard Drinks

c Front label) Whisky Single Malt Spirit Label )) - Green colour font
Title = T42 Single Malt Whisky
Crafted and aged ready to enjoy now
Bottle # _______ Cask # & Type __________

a + b back Label) Information Label (for Gin & Vodka Bottles))

Spirit distilled by Marta Drovely in Velvet Heron Stills
Bottled at Gull Reef Distillery
Saltmere, Gull Reef, Tasmania
Product of Australia (maybe use logo instead of text)
You'll find more Gull Reef made Product and Gifts at
www.gullreefdistillery.example
Mobile: 0477 SALUTE

c Back label) Whisky Single Malt Spirit Label
Distilled at: Brambleford Distillery
Western Junction, Tasmania
Bottled by Marta Drovely
Gull Reef Distillery
Product of Australia
Mobile: 0477 SALUTE

e Back label) Information label for all bottles and spirits
Recycle logo (Australian Standard)
Don't Drink While Pregnant Logo in Colour (details attached)
Blank white Angel Wings Shape shape Section (section for me to personally dedicate bottle by hand written signature)

3rd Section) mm❤ short & sweet story (yet to be finalised out of some of the info given below)

A bit more elaboration about this Project: My story is that I was made on Gull Reef and I love living a life of freedom, walking daily on our bare beaches and taking photos of this amazing unique place and always able to find a smiling and supportive face. I am very passionate about our Island, all that is has to offer including our world class quality produce, the outstanding quality brand that we are well known for by everyone and the friendly locals.

A native Lady is very exciting to be running the 1st Distillery at 40 degrees South. Making Spirits on Gull Reef in Bass Strait Tasmania, well known as the Roaring 40's. It is known to have the freshest / purest air in the world and likewise with rain water, it sure seems that was to us anyway. Also famous for the tallest lighthouse in the Southern Hemisphere built because of the large number of shipwrecks around Gull Reef, especially the Cataraqui.

My mission is to contribute more to our local economy and community and do this Island and our Industry proud, by way of building and operating a profitable first class boutique spirit distillery that can grow with demand. Using our local products and botanicals to make our very own beautiful beverages to be enjoyed by my Family, residents, visitors and those from afar.

After 7 years in design, now distilling with 2 custom made Copper 55L Pot Stills, namely my Copper Herons, that travelled across wild seas on a Cray Boat to their new home and are now making award winning spirits.
Namely Gin, using Gull Reef coastal and beachside botanicals, also Ruby Grapefruit & Ginger Vodka. In addition I will also be releasing T42 Single Malt Whisky.

To follow will be other varieties made with Local Produce such as Gull Reef apple and Gull Reef honey spirits and this range will grow with demand.

The growing Industry as I know it, the Distillers and their Teams are fun, friendly with passion and professionalism about awesome alcoholic beverages.

Gull Reef Distillery Sales will be aimed predominantly people visiting the Island. Our market is predominately Golfers, as Gull Reef has two very highly ranked Public Links Courses in Australia and the World. Websites and Podcast still to be developed will which build relationships with current and new people, share our entertaining distilling journey and provide educational information about our Industry and surrounds that make our product such great quality with the naturally amazing wild yeasts and so on.

Gull Reef Distillery will also be selling bottles online and posting orders from Gull Reef to Australia, whereby we want our final design be a simple, effective and consistent brand that shines of natural outstanding qualities of our spirits. Creating an exciting and unforgettable unboxing experience to keep our customers coming back to buy more bottles of spirits from Gull Reef Distillery.

The logo chosen will set us apart from the rest making Gull Reef Distillery easily recognisable and people will respond with a smile and buy bottles. They will be compelled to proudly share the news of their purchase and details of the Distillery far and wide on a variety of Media platforms and consistently returning for more of our delicious Products.

Bottles of Spirit made by Gull Reef Distillery will also be the new gift to give both males and females, plus a great present to give to those celebrating any occasion.
Customers will be given the opportunity for the bottle to be dedicated as a one of a kind for themselves of as a gift, hand-signed with a personalised note to the person from Merry Marta | Gull Reef Distillery.

Furthermore a series of unique hand made small batch collectables will be next in design…..

Bottles details at this stage are…. (but subject to change)

200ML & 700ML OSLO STYLE BOTTLES MARCH 2020 BOTTLES AT GR DISTILLERY
http://www.vesselmart.example/p7724qrt.html

700ml size are to be served behind bars and in restaurants
200ml make the perfect gift and travel size.
Will also be selling 200ml in gift packs of 3 in a black Jute bag with cane handles and a see through face.
Thank you so much, happy to discuss further to help with design finalisation.
mm❤
MARTA

Hello, My Sincere apologies that I have not responded sooner. Thank you all for your patience.

Target Market(s)

Golfers, award winning hand-made Spirit appreciators and collectors

Font styles to use
Other font styles liked:
• Feeling Lovely has been used previously for the mm❤

Requirements
Must have
• Stand out
Copper Background on Main Label
Nice to have
• Please see in Project description what I think would be nice. Also attached files help to visualise what I have in mind.
Should not have
• I wouldn't tell a great designer what not to do :-)

```html
<!DOCTYPE html>
<html lang="en">
<head>
<meta charset="utf-8">
<title>Gull Reef Distillery – Native Gin Labels</title>
<link rel="stylesheet" href="https://fonts.googleapis.com/css2?family=Arimo:wght@400;700&family=Great+Vibes&display=swap">
<style>
  :root {
    --paper: #ffffff;
    --label-green: #1f4a14;
    --copper-dark: #8a3a0e;
    --copper: #c9621f;
    --copper-light: #f2a45e;
    --info-text: #f0a868;
    --ink: #1a0d05;
    --field-box: #a9b9a0;
    --warn-red: #d0202a;
    --icon-ink: #000000;
  }
  html, body {
    margin: 0;
    padding: 0;
    width: 849px;
    height: 1200px;
    overflow: hidden;
    background: var(--paper);
  }
  .label-sheet {
    display: block;
    width: 849px;
    height: 1200px;
  }
  .brand-name { font-family: "Arimo", Arial, sans-serif; font-weight: 700; fill: var(--ink); }
  .neck-name { font-family: "Arimo", Arial, sans-serif; font-weight: 700; fill: var(--copper-light); }
  .product-title { font-family: "Great Vibes", cursive; fill: #3a1505; }
  .volume { font-family: "Arimo", Arial, sans-serif; fill: #ecc9a2; }
  .info-line { font-family: "Arimo", Arial, sans-serif; fill: var(--info-text); }
  .field-label { font-family: "Arimo", Arial, sans-serif; font-weight: 700; fill: #000; }
  .label-body { fill: var(--label-green); }
  .label-border { fill: none; stroke: url(#copperEdge); stroke-width: 7; }
  .label-inner-line { fill: none; stroke: var(--copper); stroke-width: 2; }
  .field-box { fill: var(--field-box); }
  .recycle-arrow { fill: none; stroke: var(--icon-ink); stroke-width: 3.5; stroke-linejoin: round; }
  .recycle-head { fill: var(--icon-ink); }
</style>
</head>
<body>
<svg class="label-sheet" viewBox="0 0 1500 2121" preserveAspectRatio="none" xmlns="http://www.w3.org/2000/svg">
  <defs>
    <linearGradient id="copperEdge" x1="0" y1="0" x2="1" y2="1">
      <stop offset="0" stop-color="#f2a45e"/>
      <stop offset="0.5" stop-color="#c9621f"/>
      <stop offset="1" stop-color="#8a3a0e"/>
    </linearGradient>
    <linearGradient id="copperScene" x1="0" y1="0" x2="0" y2="1">
      <stop offset="0" stop-color="#e47c34"/>
      <stop offset="0.55" stop-color="#b4501a"/>
      <stop offset="1" stop-color="#5e2a0c"/>
    </linearGradient>
    <linearGradient id="copperRibbon" x1="0" y1="0" x2="1" y2="0">
      <stop offset="0" stop-color="#8a3a0e"/>
      <stop offset="0.3" stop-color="#f0a060"/>
      <stop offset="0.7" stop-color="#e08a3c"/>
      <stop offset="1" stop-color="#8a3a0e"/>
    </linearGradient>
    <path id="labelShape" d="M20,65 H70 Q166,-65 262,65 H312 Q332,65 332,85 V380 Q332,400 312,400 H282 Q166,530 50,400 H20 Q0,400 0,380 V85 Q0,65 20,65 Z"/>
    <path id="labelInner" d="M32,82 H78 Q166,-30 254,82 H300 Q315,82 315,97 V370 Q315,385 300,385 H270 Q166,495 62,385 H32 Q17,385 17,370 V97 Q17,82 32,82 Z"/>
    <g id="neckBand">
      <path d="M0,0 H71 V355 L35.5,328 L0,355 Z" fill="var(--label-green)"/>
      <rect x="4" y="0" width="6" height="348" fill="var(--copper)"/>
      <rect x="61" y="0" width="6" height="348" fill="var(--copper)"/>
      <text class="neck-name" transform="translate(45,170) rotate(-90)" text-anchor="middle" font-size="28">Gull Reef Distillery</text>
    </g>
    <g id="recycleArrow">
      <path class="recycle-arrow" d="M-10,-3 L-4,-13 L4,-13"/>
      <polygon class="recycle-head" points="3,-18 10,-13 3,-8"/>
    </g>
  </defs>

  <!-- neck bands -->
  <use href="#neckBand" transform="translate(519,230)"/>
  <use href="#neckBand" transform="translate(942,230)"/>

  <!-- front label -->
  <g class="front-label" transform="translate(384,1035)">
    <use href="#labelShape" class="label-body"/>
    <use href="#labelShape" class="label-border"/>
    <use href="#labelInner" class="label-inner-line"/>
    <text class="brand-name" x="166" y="120" text-anchor="middle" font-size="30">Gull Reef</text>
    <text class="brand-name" x="166" y="150" text-anchor="middle" font-size="18">Distillery</text>
    <rect x="92" y="164" width="148" height="134" rx="10" fill="url(#copperScene)" role="img" aria-label="Outback sunset scene with two copper pot stills"/>
    <path d="M-8,320 L40,303 Q166,330 292,303 L340,320 L330,372 L292,386 Q166,408 40,386 L2,372 Z" fill="url(#copperRibbon)" role="img" aria-label="Ornamental copper scroll ribbon"/>
    <text class="product-title" x="166" y="362" text-anchor="middle" font-size="48">Native Gin</text>
    <text class="volume" x="166" y="418" text-anchor="middle" font-size="14">200 ml</text>
  </g>

  <!-- back label -->
  <g class="back-label" transform="translate(810,1035)">
    <use href="#labelShape" class="label-body"/>
    <use href="#labelShape" class="label-border"/>
    <use href="#labelInner" class="label-inner-line"/>
    <text class="brand-name" x="166" y="80" text-anchor="middle" font-size="22">Gull Reef</text>
    <text class="brand-name" x="166" y="100" text-anchor="middle" font-size="12">Distillery</text>
    <rect x="122" y="108" width="88" height="82" rx="8" fill="url(#copperScene)" role="img" aria-label="Outback scene with two copper pot stills"/>
    <g class="info-block" text-anchor="middle" font-size="10.5">
      <text class="info-line" x="166" y="206">Distilled in mm Copper Herons &amp; bottled at:</text>
      <text class="info-line" x="166" y="218">Gull Reef Distillery</text>
      <text class="info-line" x="166" y="231">Saltmere, Gull Reef, Tasmania</text>
      <text class="info-line" x="166" y="246">Product of Australia</text>
      <text class="info-line" x="166" y="261">Find more amazing beverages at</text>
      <text class="info-line" x="166" y="273">www.gullreefdistillery.example</text>
      <text class="info-line" x="166" y="289">Marta Drovely (Mobile) 0477 SALUTE</text>
    </g>
    <rect class="field-box" x="30" y="299" width="272" height="73" rx="6"/>
    <text class="field-label" x="37" y="314" font-size="9.5">Batch :</text>
    <text class="field-label" x="37" y="332" font-size="9.5">Bottle :</text>
    <text class="field-label" x="37" y="349" font-size="9.5">%Alc Vol.:</text>
    <text class="field-label" x="37" y="367" font-size="9.5">Standard Drinks:</text>
    <g class="recycle-icon" role="img" aria-label="Recycling symbol" transform="translate(142,403)">
      <circle r="21" fill="#fff" stroke="#000" stroke-width="2"/>
      <use href="#recycleArrow"/>
      <use href="#recycleArrow" transform="rotate(120)"/>
      <use href="#recycleArrow" transform="rotate(240)"/>
    </g>
    <g role="img" aria-label="Pregnancy warning symbol">
      <circle cx="196" cy="403" r="20" fill="#fff" stroke="var(--warn-red)" stroke-width="4"/>
      <line x1="182" y1="389" x2="210" y2="417" stroke="var(--warn-red)" stroke-width="4"/>
    </g>
  </g>
</svg>
</body>
</html>
```